Industrial Company needing new business cards

We are a newly branded Industrial trade company. We specialise in Electrical, Mechanical and Air-conditioning.

I would like to see designs single sided. Focusing on the color scheme white/red/black and possibly gray. Possibly make it a black card with white writting... but open to all designs.

I would like the design to be professional, sleek and to the point.

Industry/Entity Type

Business

Contact Information for Business Card

Tom Harwick
Managing Director / Electrician
tomwork@velnet.com.au
47 Garnet Road, Rutherford NSW 2320
Mobile: 0427115830
www.harwickindustrialgroup.com.au

Requirements
Must have
• Must be able to be sent in a manner that i can change the details for each employee.
• Our logo
Nice to have
• Would like it to somehow have " incorporating Talvo Group Pty Ltd" as this is the company we have taken over.
Should not have
• No yellow!!!
• must not simply place "talvo group" randomly on the business card. refer nice to have.

```html
<!DOCTYPE html>
<html lang="en">
<head>
<meta charset="utf-8">
<title>Harwick Industrial Group – Business Card</title>
<link href="https://fonts.googleapis.com/css2?family=Open+Sans:wght@400;600;700&display=swap" rel="stylesheet">
<style>
  :root {
    --backdrop: #d9d6d3;
    --card: #141414;
    --card-edge: #1d1d1d;
    --white: #ffffff;
    --text: #e9e9e9;
    --grey: #9a9a9a;
    --red: #e0141e;
  }
  * { box-sizing: border-box; margin: 0; padding: 0; }
  html, body {
    width: 1200px; height: 844px; overflow: hidden;
    background: var(--backdrop);
    font-family: "Open Sans", Arial, sans-serif;
  }
  .stage {
    width: 1200px; height: 844px;
    display: flex; align-items: center; justify-content: center; gap: 40px;
  }
  .card {
    position: relative;
    width: 540px; height: 309px;
    background: var(--card);
    border: 1px solid var(--card-edge);
    box-shadow: 0 10px 30px rgba(0,0,0,.25);
    color: var(--text);
    overflow: hidden;
  }
  .brand { position: absolute; display: flex; align-items: center; }
  .brand-mark { background: var(--red); flex: none; }
  .brand-text { display: flex; flex-direction: column; }
  .brand-name {
    color: var(--white); font-weight: 700; text-transform: uppercase;
    letter-spacing: .04em; white-space: nowrap;
  }
  .brand-tagline {
    color: var(--grey); font-weight: 400; text-transform: uppercase;
    letter-spacing: .12em; border-top: 1px solid var(--grey);
    white-space: nowrap;
  }

  /* front */
  .card-front .brand { left: 120px; top: 54px; gap: 14px; }
  .card-front .brand-mark { width: 44px; height: 44px; }
  .card-front .brand-name { font-size: 17px; line-height: 19px; border-left: 2px solid var(--white); padding-left: 10px; }
  .card-front .brand-tagline { font-size: 7px; margin-top: 6px; padding-top: 4px; }

  .contact-list {
    position: absolute; right: 36px; top: 150px;
    list-style: none; text-align: right; font-size: 12.5px; line-height: 22px;
  }
  .contact-list li { display: flex; justify-content: flex-end; align-items: center; gap: 6px; white-space: nowrap; }
  .contact-icon { width: 13px; height: 13px; background: var(--red); display: inline-flex; align-items: center; justify-content: center; }
  .contact-icon svg { width: 9px; height: 9px; }

  .person { position: absolute; left: 36px; top: 204px; }
  .person-name { color: var(--red); font-weight: 700; font-size: 17px; line-height: 22px; }
  .person-role { font-size: 13px; line-height: 18px; }
  .person-address { margin-top: 12px; font-size: 13px; line-height: 19px; font-style: normal; }

  /* back */
  .card-back .brand { left: 50%; top: 50%; transform: translate(-50%, -50%); gap: 18px; }
  .card-back .brand-mark { width: 62px; height: 62px; }
  .card-back .brand-name { font-size: 24px; line-height: 26px; border-left: 3px solid var(--white); padding-left: 12px; }
  .card-back .brand-tagline { font-size: 9px; margin-top: 8px; padding-top: 5px; }
</style>
</head>
<body>
<main class="stage">

  <section class="card card-front" aria-label="Business card, details side">
    <div class="brand">
      <span class="brand-mark"></span>
      <div class="brand-text">
        <span class="brand-name">Harwick<br>Industrial<br>Group</span>
        <span class="brand-tagline">Electrical - Mechanical - Airconditioning</span>
      </div>
    </div>

    <ul class="contact-list">
      <li>0427115830
        <span class="contact-icon"><svg viewBox="0 0 10 10"><path fill="#fff" d="M2 1h2l1 2-1 1c.5 1 1 1.5 2 2l1-1 2 1v2c-4 1-8-3-7-7z"/></svg></span>
      </li>
      <li>tomwork@velnet.com.au
        <span class="contact-icon"><svg viewBox="0 0 10 10"><rect x="1" y="2.5" width="8" height="5" fill="none" stroke="#fff" stroke-width="1"/><path d="M1 2.5l4 3 4-3" fill="none" stroke="#fff" stroke-width="1"/></svg></span>
      </li>
      <li>www.harwickindustrialgroup.com.au
        <span class="contact-icon"><svg viewBox="0 0 10 10"><path d="M4 6l2-2M3.5 4.5l-1 1a1.4 1.4 0 002 2l1-1M6.5 5.5l1-1a1.4 1.4 0 00-2-2l-1 1" fill="none" stroke="#fff" stroke-width="1"/></svg></span>
      </li>
    </ul>

    <div class="person">
      <p class="person-name">Tom Harwick</p>
      <p class="person-role">Managing Director / Electrician</p>
      <address class="person-address">47 Garnet Road,<br>Tallowby VIC 3999</address>
    </div>
  </section>

  <section class="card card-back" aria-label="Business card, brand side">
    <div class="brand">
      <span class="brand-mark"></span>
      <div class="brand-text">
        <span class="brand-name">Harwick<br>Industrial<br>Group</span>
        <span class="brand-tagline">Electrical - Mechanical - Airconditioning</span>
      </div>
    </div>
  </section>

</main>
</body>
</html>
```